Flyer-Design für ein Restaurant
Zielgruppe
Wir betreiben ein Hotel im höchsten Wintersportort Österreichs – auf 2020 Meter Seehöhe.
Im Hotel ist ein Restaurant, welches abends geöffnet hat.
Wir legen im Restaurant sehr viel wert darauf, dass alles frisch gekocht wird und keinerlei Fertig-Produkte verarbeitet werden. Außerdem haben wir einen Holzkohlegrill wo die Steaks auf offenem Feuer gegrillt werden.
Vielleicht kann man irgendwie ein Foto von Feuer / Holzkohle oder so einbauen.
Im Ort gibt es allerhand Ferienwohnungen und auch Mitarbeiter die gerne am Abend essen gehen möchten.
genau das ist unser Klientel, das wir ansprechen möchten.
Die Flyer werden in den Betrieben wie Sportgeschäften / Skischulen etc. aufgelegt
Der Flyer soll durch seine Aufmachung / Design / Fotos den Wunsch wachsen lassen, dass man dort mal Essen gehen muss !
Aufgabenstellung
Wir haben uns für das quadratische Format 148 x 148mm entschieden – also ein Falzflyer mit 4 Seiten.
Falls man den Inhalt nicht auf 4 Seiten unterbringt, dann auch mit 6 Seiten möglich
Druckvorgabe liegt als Datei bei
Auf alle Fälle sollte im Flyer enthalten sein:
• Logo
• Telefonnummer für Tischreservierung (+43/5127/3861-417)
• Karte wie man uns findet
• Foto vom Hotel
• Adresse (Bergblick Residenz - Almrosenweg 9 - 6471 Lerchfeld)
• Auszüge aus der Speisekarte (ohne Preise) (Speisekarte ist als PDF dabei)
• Öffnungszeiten 18:00 – 21:00
• Kindergerichte
Ich werde unter der Adresse www.talvoro-demo.ag/flyer/
etliche Fotos hochladen vom Haus...daraus können Sie das ideale Foto raussuchen
Unsere Homepage ist www.bergwerkel.at - Muss aber nicht im Design oder dgl. zusammenpassen - ist eh schon alt !
Drucken lassen wir es bei druckvelo.at
Druckhinweise: https://www.druckvelo.at/p/falzflyer-a5-quadrat

```html
<!DOCTYPE html>
<html lang="de">
<head>
<meta charset="utf-8">
<title>Aus dem Holzkohlegrill – Speisekarte</title>
<link href="https://fonts.googleapis.com/css2?family=Gelasio:wght@600;700&family=Open+Sans:wght@400;500&display=swap" rel="stylesheet">
<style>
  :root {
    --stage: #e9e9eb;
    --paper: #ffffff;
    --brown: #5b4038;
    --brown-soft: #7c6d67;
    --ember-dark: #0b0807;
    --ember-mid: #3a1a0e;
    --ember-hot: #b9501a;
    --ember-glow: #ef9b34;
    --ornament: #6a4c42;
  }
  * { margin: 0; padding: 0; box-sizing: border-box; }
  html, body {
    width: 1200px; height: 664px; overflow: hidden;
    background: var(--stage);
  }
  .spread {
    position: absolute; left: 40px; top: 52px;
    width: 1120px; height: 560px;
    display: flex;
    box-shadow: 0 6px 24px rgba(0,0,0,.18);
  }
  .page { position: relative; width: 560px; height: 560px; overflow: hidden; }

  /* Left page: grill photo */
  .page--grill { background: var(--ember-dark); }
  .grill-photo {
    position: absolute; inset: 0;
    background:
      radial-gradient(ellipse 65% 30% at 50% 58%, #7a3c22 0%, transparent 75%),
      radial-gradient(ellipse 40% 25% at 35% 38%, #5e2e1a 0%, transparent 75%),
      linear-gradient(180deg, var(--ember-dark) 0%, #1c0f0a 28%, var(--ember-mid) 48%, var(--ember-hot) 80%, var(--ember-glow) 100%);
  }
  .cut-list {
    position: absolute; top: 22px; left: 387px;
    width: 180px; text-align: center;
    color: #fff; font-family: "Gelasio", serif;
  }
  .cut { margin-bottom: 12px; }
  .cut__name { font-size: 19px; font-weight: 700; letter-spacing: .8px; line-height: 1.1; }
  .cut__weight { font-size: 12px; font-weight: 600; letter-spacing: .6px; line-height: 1.2; }

  /* Right page: menu */
  .page--menu { background: var(--paper); color: var(--brown); }
  .menu-head {
    position: absolute; top: 24px; left: 0; width: 100%;
    text-align: center;
  }
  .menu-title {
    font-family: "Gelasio", serif; font-weight: 700;
    font-size: 31px; letter-spacing: .4px; line-height: 1;
  }
  .menu-subtitle {
    font-family: "Open Sans", sans-serif; font-size: 12.5px; margin-top: 3px;
  }
  .ornament {
    display: block; margin: 6px auto 0;
    width: 210px; height: 42px;
  }
  .sides {
    position: absolute; top: 128px; left: 0; width: 100%;
    text-align: center;
  }
  .sides__title {
    font-family: "Gelasio", serif; font-weight: 700; font-size: 19px; letter-spacing: .6px;
  }
  .sides__list {
    font-family: "Open Sans", sans-serif; font-size: 13.5px; margin-top: 2px;
  }
  .dish { position: absolute; left: 17px; display: flex; align-items: center; }
  .dish--tagliata { top: 222px; }
  .dish--pork { top: 378px; }
  .dish__photo { flex: none; }
  .dish--tagliata .dish__photo {
    width: 156px; height: 136px; margin-right: 30px;
    background: linear-gradient(160deg, #8a6a50 0%, #d9cfc4 28%, #f3f0ed 55%, #6f8f4a 85%, #c9c2bb 100%);
  }
  .dish--pork .dish__photo {
    width: 164px; height: 144px; margin-right: 36px;
    background: linear-gradient(135deg, #d9c48e 0%, #c28a4d 45%, #dcc995 100%);
  }
  .dish__name {
    font-family: "Gelasio", serif; font-weight: 700; font-size: 18px; letter-spacing: .6px;
    line-height: 1.2;
  }
  .dish__desc {
    font-family: "Open Sans", sans-serif; font-size: 13px; line-height: 1.45;
    color: var(--brown-soft);
  }
  .dish--tagliata .dish__text { margin-top: -28px; }
  .dish--pork .dish__text { margin-top: 4px; }
</style>
</head>
<body>
  <main class="spread">
    <section class="page page--grill">
      <div class="grill-photo" role="img" aria-label="Foto: Steaks mit Rosmarin und Chili auf dem Holzkohlegrill über offenem Feuer"></div>
      <div class="cut-list">
        <div class="cut"><div class="cut__name">Filetsteak</div><div class="cut__weight">250g</div></div>
        <div class="cut"><div class="cut__name">Ribeysteak</div><div class="cut__weight">300g</div></div>
      </div>
    </section>

    <section class="page page--menu">
      <header class="menu-head">
        <h1 class="menu-title">Aus dem Holzkohlegrill</h1>
        <p class="menu-subtitle">bei offenem Feuer und 350°</p>
        <svg class="ornament" viewBox="0 0 210 42" role="img" aria-label="Verziertes Trennornament">
          <rect x="0" y="19" width="210" height="4" rx="2" fill="var(--ornament)" opacity=".18"/>
          <rect x="80" y="6" width="50" height="30" rx="15" fill="var(--ornament)" opacity=".22"/>
        </svg>
      </header>

      <div class="sides">
        <h2 class="sides__title">Alle Steaks servieren wir mit</h2>
        <p class="sides__list">Gemüse / Pommes frites / 2 kalte Saucen / Kräuterbutter</p>
      </div>

      <article class="dish dish--tagliata">
        <div class="dish__photo" role="img" aria-label="Foto: Tagliata mit Rucola, Kirschtomaten und Parmesan"></div>
        <div class="dish__text">
          <h3 class="dish__name">Tagliata</h3>
          <p class="dish__desc">250g vom Rumpsteak<br>in Streifen geschnitten dazu<br>Rucola / Kirschtomaten / Parmesan</p>
        </div>
      </article>

      <article class="dish dish--pork">
        <div class="dish__photo" role="img" aria-label="Foto: Schweinerückensteaks in Senfsauce"></div>
        <div class="dish__text">
          <h3 class="dish__name">Schweinerückensteak</h3>
          <p class="dish__desc">Senfsauce / Gemüse / Pommes frites</p>
        </div>
      </article>
    </section>
  </main>
</body>
</html>
```